I have a tallow based business and I want to streamline my products

I have roughly 10 items that I would like to make lebals for in order to streamline my business, I am attaching the current design and am willing to work with this but would also like to see if you come up with something different, my biggest seller is my facewash , my webpage is themeadowlyco,com my current designs are below- The newest one is the light brown version which I do like but I am not sure how that will integrate or be streamlined with the remaining products, If you believe it can look similar and still be attractive, I am ok with that too,

My current Label Project Needs:

Tallow + Magnesium Lotion biodegradable wheat bottle
Tallow Cream Face Wash - biodegradable what bottle
Tallow Body Butter 8 oz jar with bamboo lid
Tallow Deodorant will be printed on a Kraft Paper tube
Tallow Face Cream for Day wear 2 oz glass jar with bamboo lid
Vitamin C Serum 2 oz serum bottle with bamboo pump
Blue Algae Toner 4 oz glass bottle
Tallow + Hyaluronic 2oz face cream jar
'
My project is to display sustainable products, eco friendly packaging, organic , natural and holistic

I am ok with the newest label I attached but I am also ok with a minimalistic project, I would love to choose from a couple of designs.

Thank you so much

```html
<!DOCTYPE html>
<html lang="en">
<head>
<meta charset="utf-8">
<title>Meadowly Pure Organics – Face Cream Label</title>
<link href="https://fonts.googleapis.com/css2?family=Jost:wght@400;500;600&family=Tenor+Sans&family=Lato:wght@400&family=Libre+Baskerville:wght@700&display=swap" rel="stylesheet">
<style>
  :root {
    --page: #ffffff;
    --ink: #3f2e2c;
    --gold: #e0b363;
    --gold-soft: #ecc886;
    --rule: #d9d9d9;
    --frame: #cfcfcf;
  }
  * { box-sizing: border-box; margin: 0; padding: 0; }
  html, body { width: 1200px; height: 1200px; overflow: hidden; background: var(--page); }
  .canvas { position: relative; width: 1200px; height: 1200px; }
  .label {
    position: absolute; left: 40px; top: 305px;
    width: 1045px; height: 550px;
    transform: scale(1.0718); transform-origin: 0 0;
    background: var(--page);
    border: 2px solid var(--frame);
    box-shadow: 0 18px 22px -14px rgba(0,0,0,.25);
    color: var(--ink);
  }
  /* benefits column */
  .benefits { position: absolute; left: 60px; top: 25px; width: 240px; list-style: none; }
  .benefit {
    display: flex; align-items: center; height: 98px;
    border-bottom: 1px solid var(--rule);
    font-family: "Jost", sans-serif; font-weight: 500; font-size: 19px; line-height: 1.05;
  }
  .benefit:last-child { border-bottom: none; }
  .benefit-icon { width: 40px; height: 40px; margin: 0 24px 0 36px; flex: none; }
  .maker {
    position: absolute; left: 60px; top: 428px; width: 241px; height: 81px;
    border: 1.5px solid var(--ink); border-radius: 4px;
    font-family: "Jost", sans-serif; font-size: 10.5px; text-align: center;
    line-height: 1.55; padding-top: 8px;
  }
  .maker strong { font-weight: 600; }
  /* centre panel */
  .front { position: absolute; left: 320px; top: 0; width: 450px; height: 100%; text-align: center; }
  .brand-dot { position: absolute; left: 217px; top: 28px; width: 16px; height: 16px; border-radius: 50%; background: var(--gold); }
  .brand { position: absolute; top: 84px; width: 100%; font-family: "Tenor Sans", sans-serif; font-size: 19.5px; letter-spacing: 2.2px; }
  .product { position: absolute; top: 118px; width: 100%; font-family: "Jost", sans-serif; font-weight: 600; font-size: 66px; letter-spacing: 0.5px; }
  .variant {
    position: absolute; left: 95px; top: 212px; width: 260px; height: 40px;
    background: var(--gold); color: #fff; border-radius: 6px 14px 6px 14px;
    font-family: "Jost", sans-serif; font-size: 25px; letter-spacing: 1px; line-height: 40px;
  }
  .animal-art { position: absolute; left: 135px; top: 295px; width: 172px; height: 130px; border-radius: 8px; background: linear-gradient(160deg, #4a3634, #3a2a28); }
  .tagline { position: absolute; top: 436px; width: 100%; font-family: "Jost", sans-serif; font-weight: 500; font-size: 33px; }
  .tagline .sep { color: var(--gold); font-size: 20px; vertical-align: 6px; padding: 0 4px; }
  .net { position: absolute; top: 496px; width: 100%; font-family: "Jost", sans-serif; font-size: 17px; }
  /* ingredients */
  .ingredients-title {
    position: absolute; left: 822px; top: 255px; width: 28px; height: 260px;
    background: var(--gold); color: #fff;
    writing-mode: vertical-rl; transform: rotate(180deg);
    font-family: "Libre Baskerville", serif; font-weight: 700; font-size: 15px;
    text-align: center; line-height: 28px;
  }
  .ingredients {
    position: absolute; left: 862px; top: 28px; width: 152px; height: 488px;
    writing-mode: vertical-rl; transform: rotate(180deg);
    font-family: "Lato", sans-serif; font-size: 13.4px; line-height: 19px;
    letter-spacing: 0.6px; text-align: justify;
  }
</style>
</head>
<body>
<main class="canvas">
  <section class="label">
    <ul class="benefits">
      <li class="benefit"><svg class="benefit-icon" role="img" aria-label="Cow head icon" viewBox="0 0 40 40"><circle cx="20" cy="20" r="16" fill="none" stroke="var(--gold)" stroke-width="2"/></svg>Grass Tallow</li>
      <li class="benefit"><svg class="benefit-icon" role="img" aria-label="Leaf in circle icon" viewBox="0 0 40 40"><circle cx="20" cy="20" r="16" fill="none" stroke="var(--gold)" stroke-width="2"/></svg>Organic<br>Ingredients</li>
      <li class="benefit"><svg class="benefit-icon" role="img" aria-label="Hands with heart icon" viewBox="0 0 40 40"><circle cx="20" cy="20" r="16" fill="none" stroke="var(--gold)" stroke-width="2"/></svg>Hand Crafted</li>
      <li class="benefit"><svg class="benefit-icon" role="img" aria-label="Handshake icon" viewBox="0 0 40 40"><circle cx="20" cy="20" r="16" fill="none" stroke="var(--gold)" stroke-width="2"/></svg>Fair Trade</li>
    </ul>
    <div class="maker">MANUFACTURED BY<br><strong>MEADOWLY PURE ORGANICS</strong><br>PO. BOX : 4172 FERNBROOK, VA 23801<br>meadowlypureorganics.com</div>

    <div class="front">
      <span class="brand-dot"></span>
      <p class="brand">MEADOWLY PURE ORGANICS</p>
      <h1 class="product">FACE CREAM</h1>
      <p class="variant">TALLOW CREAM</p>
      <div class="animal-art" role="img" aria-label="Dark brown cow silhouette"></div>
      <p class="tagline">Cleanse<span class="sep">•</span>Purify<span class="sep">•</span>Moisturize</p>
      <p class="net">NET WT. 8 OZ (236ML)</p>
    </div>

    <h2 class="ingredients-title">Our Amazing Ingredients:</h2>
    <p class="ingredients">Distilled Water, Lavender Hydrosol, Glycerin, Grass Fed Tallow, Daucus Carota (Carrot Seed Oil), Oenothera Biennis (Rosehip Oil), Simmondsia Chinensis(Jojoba Oil) Cocos Nucifera (Coconut Oil), Cucurbita Pepo Seed Oil (Pumpkin Seed Oil)Coenzyme Q10 ( CoQ10 )Niacinamide, Vitamin B3 Citrus Paradisi Seed Oil (Grapefruit Seed oil), Decyl Glucoside, Cetyl Alcohol Citric Acid, Xanthan Gum, Sodium Benzoate (Preservative)</p>
  </section>
</main>
</body>
</html>
```